Thornwell Building Company - advertisement poster

I am looking to print some canvas signs to advertise my general contracting company, Thornwell Building Company. The sign will measure 6' long x 3' high so the size should match that ratio. I already have a logo icon, which is the Letter 'A' and some trees that I would like to incorporate, see attached. I would also like the to have the following information listed:
1) phone number: 472-318-6095
2) email: thornwellbuildingcompany@mailvistra.net
3) website: thornwellbuildingcompany.com
4) Lic#5386204
5) I want to use this text: "BUILD WITH THE T-CREW!"

The ad should be relatively simple and clean. Black and Green are my company colors. I am open to creative ideas!

Target Market(s)

People looking to renovate their homes

Industry/Entity Type

Construction

Colors
59FF00
82FF00
B8FF75
E3FFCB
F4FFEA

Requirements
Must have
• Must have my company logo
Should not have
• No photos or complex graphics

```html
<!DOCTYPE html>
<html lang="en">
<head>
<meta charset="utf-8">
<title>Thornwell Building Company – Sign</title>
<link rel="stylesheet" href="https://fonts.googleapis.com/css2?family=Krona+One&family=Lato:ital,wght@1,700&display=swap">
<style>
  :root {
    --page: #eef1f4;
    --bar: #9ad557;
    --green: #73b54f;
    --green-muted: #7daf5d;
    --divider: #5e9a43;
    --black: #000000;
    --white: #ffffff;
    --contact-text: #eef4e8;
  }
  * { margin: 0; padding: 0; box-sizing: border-box; }
  html, body {
    width: 1200px; height: 927px; overflow: hidden;
    background: var(--page);
  }
  .sign {
    position: absolute; left: 40px; top: 171px;
    width: 1120px; height: 585px;
    display: flex; flex-direction: column;
    box-shadow: 0 10px 28px rgba(0,0,0,0.18);
  }
  .sign__bar { height: 12px; background: var(--bar); flex: none; }
  .sign__body { flex: 1; display: flex; }

  .promo {
    width: 615px; position: relative;
    background: linear-gradient(var(--green) 0 382px, var(--green-muted) 382px 100%);
  }
  .promo__kicker {
    position: absolute; left: 0; width: 615px; top: 226px;
    text-align: center; color: var(--white);
    font-family: "Krona One", sans-serif; font-size: 20px; letter-spacing: 5px;
    line-height: 1;
  }
  .promo__headline {
    position: absolute; left: 0; width: 615px; top: 262px;
    text-align: center; color: var(--white);
    font-family: "Krona One", sans-serif; font-weight: 400; font-size: 56px; letter-spacing: 4px;
    line-height: 1;
  }
  .contact {
    position: absolute; left: 186px; top: 414px;
    list-style: none;
  }
  .contact__rule {
    position: absolute; left: 216px; top: 412px;
    width: 2px; height: 118px; background: var(--divider);
  }
  .contact__item {
    display: flex; align-items: center; height: 39px;
  }
  .contact__icon { width: 18px; height: 18px; margin-right: 26px; flex: none; }
  .contact__text {
    font-family: "Lato", sans-serif; font-style: italic; font-weight: 700;
    font-size: 15.5px; color: var(--contact-text);
  }

  .brand {
    flex: 1; background: var(--black); position: relative;
  }
  .brand__name {
    position: absolute; left: 0; right: 0; top: 300px;
    display: flex; align-items: center; justify-content: center; gap: 16px;
  }
  .brand__square { width: 52px; height: 52px; background: var(--green); flex: none; }
  .brand__text {
    font-family: "Krona One", sans-serif; font-size: 21px; line-height: 1.4;
    color: var(--white); letter-spacing: 1px;
  }
  .brand__license {
    position: absolute; right: 90px; top: 400px;
    font-family: "Lato", sans-serif; font-style: italic; font-weight: 700;
    font-size: 11px; color: var(--white);
  }
</style>
</head>
<body>
  <main class="sign">
    <div class="sign__bar"></div>
    <div class="sign__body">
      <section class="promo">
        <p class="promo__kicker">BUILD WITH THE</p>
        <h1 class="promo__headline">T-CREW!</h1>
        <div class="contact__rule"></div>
        <ul class="contact">
          <li class="contact__item">
            <svg class="contact__icon" viewBox="0 0 24 24" aria-hidden="true"><path fill="#eef4e8" d="M6.6 2.5l3 3.4-1.8 2.4c1.3 2.8 3.3 4.9 6 6.2l2.4-1.8 3.4 3-1.4 3.3C10.5 18.6 5.2 13.4 3.3 5.3z"/></svg>
            <span class="contact__text">472-318-6095</span>
          </li>
          <li class="contact__item">
            <svg class="contact__icon" viewBox="0 0 24 24" aria-hidden="true"><g fill="none" stroke="#eef4e8" stroke-width="1.8"><circle cx="12" cy="12" r="9.5"/><ellipse cx="12" cy="12" rx="4.2" ry="9.5"/><path d="M2.5 12h19M4 7h16M4 17h16"/></g></svg>
            <span class="contact__text">thornwellbuildingcompany@mailvistra.net</span>
          </li>
          <li class="contact__item">
            <svg class="contact__icon" viewBox="0 0 24 24" aria-hidden="true"><g fill="none" stroke="#eef4e8" stroke-width="1.6"><rect x="2" y="5" width="20" height="14"/><path d="M2 5l10 8 10-8M2 19l7.5-7M22 19l-7.5-7"/></g></svg>
            <span class="contact__text">thornwellbuildingcompany.com</span>
          </li>
        </ul>
      </section>
      <section class="brand">
        <div class="brand__name">
          <div class="brand__square"></div>
          <div class="brand__text">THORNWELL<br>BUILDING COMPANY</div>
        </div>
        <p class="brand__license">Lic#5386204</p>
      </section>
    </div>
    <div class="sign__bar"></div>
  </main>
</body>
</html>
```